Personal Business Card

Looking for a clean and modern personal business card. Basically I need something catchy to give to potential clients and people I meet. I do a lot of freelancing (from DJ'ing to wedding videography, but its mostly on the event side of things) so it's more-so about selling myself rather than identifying with a company. I'm starting to meet more people that I want to work with after meeting them so I'm revamping my business cards.

I'm looking for a clean and modern design- I know that's really vague but I'm fine with anything ranging from a symbol to just a fancy version of my name.

Details I need on the front:
Dennis Kowal
dennis@denniskowal-mail.net
(555) 807-2291

On the back I'd like to have something simple like "Nice to have met you today" or "Great meeting you".

UPDATE 9/27 Noon: My apologies for not putting it up before- I'm definitely looking for full color. Doesn't have to be a rainbow but I am looking for the least amount of blank white as possible.

UPDATE 10/1: Really impressed with what I've been getting so far and I'm working on giving everyone feedback- if your design is still up then you're still in the run. Looking for something more unique and modern so please do not post something that looks like a template from Cardloom!

Target Market(s)

Mainly to give to people aged 18-35. Most of my encounters will be casual so the card should have a "young" feeling to it. I rarely do anything in the corporate world so it doesn't have to be boring. It should give the impression that I'm the one they should go to if they need what I do (again it changes every weekend so I'll probably say the "what I do" part.

Industry/Entity Type

Wedding

Requirements
Must have
• Basically the contact information listed above
Nice to have
• I really like the colors Blue, Silver, and Purple. They don't have to necessarily all be there though. I do like the look of polished metal if that makes sense.
Should not have
• A template that resembles card-loom. I'm in a point in my life where I'm working a lot of different markets/areas so the card does not need to have an address or address placeholder.

```html
<!DOCTYPE html>
<html lang="en">
<head>
<meta charset="utf-8">
<title>Dennis Kowal — Business Card</title>
<link rel="stylesheet" href="https://fonts.googleapis.com/css2?family=Mulish:wght@300;400;600&display=swap">
<style>
  :root {
    --backdrop: #000000;
    --card-paper: #f3f3f3;
    --ink: #222222;
    --accent-purple: #6a2f95;
    --blue-deep: #0a57a3;
    --blue-mid: #1677c2;
    --blue-bright: #05a9e6;
    --blue-steel: #3a72b5;
  }
  * { margin: 0; padding: 0; box-sizing: border-box; }
  html, body {
    width: 1200px;
    height: 1000px;
    overflow: hidden;
    background: var(--backdrop);
    font-family: "Mulish", sans-serif;
    color: var(--ink);
  }
  .canvas { position: relative; width: 1200px; height: 1000px; }

  .card {
    position: absolute;
    width: 561px;
    height: 321px;
    background: var(--card-paper);
    border-radius: 66px 0 66px 0;
    overflow: hidden;
  }
  .card--front { left: 333px; top: 142px; }
  .card--back { left: 322px; top: 510px; }

  .card__pattern {
    position: absolute;
    left: 0; top: 0;
    width: 561px; height: 321px;
  }

  .brand-square {
    position: absolute;
    right: 23px; top: 23px;
    width: 48px; height: 48px;
    border-radius: 6px;
    background: linear-gradient(135deg, var(--blue-bright), var(--blue-deep) 70%, var(--blue-steel));
  }

  .owner-name {
    position: absolute;
    right: 25px; top: 82px;
    font-size: 22px;
    font-weight: 400;
    letter-spacing: 0.2px;
  }
  .owner-name .initial { color: var(--accent-purple); }

  .contact {
    position: absolute;
    right: 25px; top: 162px;
    text-align: right;
  }
  .contact__email { font-size: 17px; font-weight: 400; line-height: 22px; }
  .contact__phone { font-size: 25px; font-weight: 300; line-height: 32px; letter-spacing: 0.3px; }

  .back-message {
    position: absolute;
    left: 0; right: 0; top: 145px;
    text-align: center;
    font-size: 17px;
    font-weight: 600;
    padding-right: 10px;
  }
</style>
</head>
<body>
<main class="canvas">
  <section class="card card--front">
    <svg class="card__pattern" viewBox="0 0 561 321" role="img" aria-label="Decorative wave of rounded blue tiles rising from the lower left">
      <defs>
        <linearGradient id="tileWave" x1="0" y1="0" x2="1" y2="0">
          <stop offset="0" stop-color="var(--blue-steel)"/>
          <stop offset="0.25" stop-color="var(--blue-deep)"/>
          <stop offset="0.45" stop-color="var(--blue-bright)"/>
          <stop offset="1" stop-color="var(--blue-mid)"/>
        </linearGradient>
      </defs>
      <polygon points="0,168 95,162 210,200 300,212 420,240 561,290 561,321 0,321" fill="url(#tileWave)"/>
    </svg>

    <div class="brand-square" aria-hidden="true"></div>
    <h1 class="owner-name"><span class="initial">D</span>ennis <span class="initial">K</span>owal</h1>
    <div class="contact">
      <p class="contact__email">dennis@denniskowal-mail.net</p>
      <p class="contact__phone">(555) 807-2291</p>
    </div>
  </section>

  <section class="card card--back">
    <p class="back-message">have a great day</p>
  </section>
</main>
</body>
</html>
```